Geek Gala Milwaukee monthly event poster template. Help make nerds cool!

We need a template for Geek Gala Milwaukee, a monthly event event that features three speakers on various topics. Geek Gala happens in cities worldwide but we need a pretty poster to list several details each month:
1. Geek Gala Milwaukee
2. Location
3. Time + date
4. Include the Geek Gala glasses (file options attached)
5. Something with the Milwaukee skyline or the outline of the shoreline with Lake Michigan or "Nerd iconography" (see below)
6. The colors white, orange, and blue.

Sorry for the short duration on this. I'm overwhelmed this week. Email with any questions. See GeekGala.com for other info. First event details will be Bramblewick Coffee Tillery Corner, 7:30pm July 22nd

Target Market(s)

Coffee shop patrons, academics, hipsters, aged 21-40.

Industry/Entity Type

Event

Font styles to use
Serif

Colors
0493ce
f37122
ffffff

Requirements
Must have
• Geek Gala glasses
• "Geek Gala Milwaukee"
• Customizable slots for Location, Time, Date
Nice to have
• Something uniquely Milwaukee and/or a variety of "nerd" iconography (Telescope, microscope, plants, film, camera, monsters, pen, paintbrush, books)

```html
<!DOCTYPE html>
<html lang="en">
<head>
<meta charset="utf-8">
<title>Geek Gala Milwaukee</title>
<link rel="stylesheet" href="https://fonts.googleapis.com/css2?family=Arimo:wght@400&display=swap">
<style>
  :root {
    --orange: #f37122;
    --blue: #0493ce;
    --white: #ffffff;
    --ink: #000000;
    --frame-fill: #f7f7f7;
  }
  * { margin: 0; padding: 0; box-sizing: border-box; }
  html, body { width: 1200px; height: 1000px; overflow: hidden; }
  body { font-family: "Arimo", Arial, sans-serif; }

  .poster {
    position: relative;
    width: 1200px;
    height: 1000px;
    background: var(--orange);
    overflow: hidden;
  }

  .brand-mark {
    position: absolute;
    left: 20px;
    top: 166px;
    display: flex;
    align-items: center;
    gap: 12px;
    color: var(--white);
    font-size: 40px;
    line-height: 1;
  }
  .brand-mark__dot {
    width: 22px;
    height: 22px;
    border-radius: 50%;
    background: var(--white);
  }

  .event-title {
    position: absolute;
    left: 338px;
    top: 66px;
    font-size: 68px;
    font-weight: 400;
    color: var(--blue);
    line-height: 1.1;
    white-space: nowrap;
  }

  .tagline {
    position: absolute;
    left: 340px;
    top: 181px;
    font-size: 41px;
    line-height: 56px;
    letter-spacing: 2.4px;
    color: var(--white);
    white-space: nowrap;
  }

  .description {
    position: absolute;
    left: 12px;
    top: 406px;
    font-size: 32px;
    line-height: 43px;
    letter-spacing: 0.7px;
    color: var(--white);
    white-space: nowrap;
  }

  .film-strip {
    position: absolute;
    left: 10px;
    top: 728px;
  }
  .film-strip__slot {
    position: absolute;
    font-size: 31px;
    line-height: 41px;
    color: var(--blue);
    white-space: nowrap;
  }
  .film-strip__slot--location { left: 44px; top: 70px; }
  .film-strip__slot--datetime { left: 420px; top: 90px; }

  .telescope-art {
    position: absolute;
    left: 862px;
    top: 676px;
    width: 336px;
    height: 300px;
    border-radius: 12px;
    background: radial-gradient(ellipse at 45% 40%, #1a1a1a 0%, #3a2414 55%, var(--orange) 100%);
  }
</style>
</head>
<body>
  <main class="poster">
    <div class="brand-mark">
      <span class="brand-mark__dot"></span>
      <span class="brand-mark__name">Geek Gala</span>
    </div>

    <h1 class="event-title">Geek Gala Milwaukee</h1>

    <p class="tagline">We all know that learning is more<br>fun when you’re drinking with<br>friends and colleagues</p>

    <p class="description">Geek Gala event during which several folks give<br>18-21-minute fun end informative presentations<br>across all disciplines I while the audience drinks<br>along</p>

    <div class="film-strip">
      <svg width="768" height="232" viewBox="0 0 768 232" aria-hidden="true">
        <rect x="0" y="0" width="768" height="232" fill="var(--ink)"/>
        <g fill="var(--white)">
          <rect x="13" y="12" width="42" height="13"/>
          <rect x="98" y="12" width="42" height="13"/>
          <rect x="183" y="12" width="42" height="13"/>
          <rect x="268" y="12" width="42" height="13"/>
          <rect x="353" y="12" width="42" height="13"/>
          <rect x="438" y="12" width="42" height="13"/>
          <rect x="523" y="12" width="42" height="13"/>
          <rect x="608" y="12" width="42" height="13"/>
          <rect x="693" y="12" width="42" height="13"/>
          <rect x="13" y="206" width="42" height="13"/>
          <rect x="98" y="206" width="42" height="13"/>
          <rect x="183" y="206" width="42" height="13"/>
          <rect x="268" y="206" width="42" height="13"/>
          <rect x="353" y="206" width="42" height="13"/>
          <rect x="438" y="206" width="42" height="13"/>
          <rect x="523" y="206" width="42" height="13"/>
          <rect x="608" y="206" width="42" height="13"/>
          <rect x="693" y="206" width="42" height="13"/>
        </g>
        <rect x="8" y="38" width="359" height="150" fill="var(--frame-fill)"/>
        <rect x="387" y="40" width="360" height="150" fill="var(--frame-fill)"/>
      </svg>
      <p class="film-strip__slot film-strip__slot--location">Bramblewick Coffee<br>Tillery Corner</p>
      <p class="film-strip__slot film-strip__slot--datetime">7:30pm July 22nd</p>
    </div>

    <div class="telescope-art" role="img" aria-label="Black illustration of a telescope on a tripod"></div>
  </main>
</body>
</html>
```